Launch of a new Investment fund

Im looking for someone design a logo and website for my Investment fund located in Singapore.

Attached to this project you will find a project scope document that details exactly what i am looking for and also includes a website copy that i have written up. I am happy for you to take your own inspiration as well to design the website. At this stage the website wont be very detailed as there isn't much information to showcase. I will require the website to be easily editable in the future so i can update it with progress the fund makes.

If you require any further details on the project please reach out to me

Coding

Coded - Design and coding required

Number of Pages Required

4 page

```html
<!DOCTYPE html>
<html lang="en">
<head>
<meta charset="utf-8">
<title>Keystar Capital Management</title>
<link href="https://fonts.googleapis.com/css2?family=Bebas+Neue&family=Open+Sans:wght@600&family=Poppins:wght@400;500&display=swap" rel="stylesheet">
<style>
:root{
  --ink:#161616;
  --text:#444;
  --muted:#666;
  --blue:#0f8fd3;
  --blue-dark:#0b7ab6;
  --dark:#17191c;
  --panel:#f6f6f6;
  --section-grey:#ededed;
  --white:#fff;
}
*{margin:0;padding:0;box-sizing:border-box}
html,body{width:1200px;height:5226px;overflow:hidden}
body{position:relative;background:var(--white);font-family:'Poppins',sans-serif;color:var(--text)}
.abs{position:absolute}
.display{font-family:'Bebas Neue',sans-serif;color:var(--ink);font-weight:400;line-height:1}

/* header */
.site-header{left:0;top:0;width:1200px;height:132px;background:var(--white)}
.brand{left:84px;top:44px;display:flex;align-items:center;gap:12px}
.brand-mark{width:40px;height:40px;background:var(--ink)}
.brand-name{font-family:'Bebas Neue',sans-serif;font-size:30px;line-height:1;color:var(--ink);letter-spacing:1px;width:180px}
.main-nav{top:62px;left:0;width:1200px;height:20px}
.main-nav a{position:absolute;font-size:13px;color:#333;text-decoration:none;letter-spacing:.3px}
.main-nav a.active::after{content:"";position:absolute;left:0;right:0;top:26px;height:3px;background:var(--blue)}

/* hero */
.hero{left:0;top:132px;width:1200px;height:692px;background:linear-gradient(100deg,#2a2420 0%,#1b2433 30%,#17305a 55%,#123a4a 75%,#0f2233 100%)}
.hero-photo{position:absolute;inset:0;background:radial-gradient(ellipse at 85% 30%,rgba(40,170,110,.45),transparent 55%),radial-gradient(ellipse at 10% 60%,rgba(120,90,70,.55),transparent 45%)}
.play{left:548px;top:300px}
.hero-title{left:0;top:436px;width:1200px;text-align:center;font-size:84px;line-height:112px;color:var(--white)}

/* about */
.photo{background:linear-gradient(160deg,#35506e,#1a2333)}
.about-img-a{left:73px;top:1015px;width:370px;height:325px;background:linear-gradient(180deg,#5a6f8e 0%,#c9855a 30%,#1c2533 55%,#0d1218 100%)}
.about-img-b{left:207px;top:1289px;width:294px;height:203px;background:linear-gradient(135deg,#2a4f86,#1a2438 60%,#33466a);border-top:4px solid #fff;border-left:4px solid #fff}
.section-title{font-size:70px}
.eyebrow{font-size:30px;color:var(--blue);letter-spacing:3px;display:flex;align-items:center;gap:14px;font-weight:400}
.eyebrow::after{content:"";width:62px;height:2px;background:#333}
.body-copy{font-size:14.5px;line-height:25.6px;color:var(--text)}

/* team */
.team-eyebrow{font-size:24px;color:var(--blue);letter-spacing:.5px}
.team-heading{font-size:25px;font-weight:500;color:var(--ink)}
.founder-photo{left:650px;top:1728px;width:465px;height:493px;background:linear-gradient(180deg,#b7b9ba 0%,#8e9296 45%,#2b3f86 65%,#6d6f72 100%)}

/* investments */
.investments{left:0;top:2412px;width:1200px;height:1624px;background:var(--section-grey);overflow:hidden}
.inv-title{left:0;top:118px;width:1200px;text-align:center;font-size:78px}
.inv-intro{left:250px;top:228px;width:700px;text-align:center;font-size:14.5px;line-height:22px;color:#333}
.card{width:400px;height:552px;background:var(--white);box-shadow:0 4px 14px rgba(0,0,0,.12);text-align:center}
.card-img{width:400px;height:306px}
.card h3{font-family:'Open Sans',sans-serif;font-weight:600;font-size:20px;color:var(--blue);letter-spacing:.4px;margin-top:30px}
.card .rule{width:50px;height:2px;background:#222;margin:16px auto 18px}
.card p{font-size:14.5px;line-height:26px;color:var(--muted);padding:0 28px}

/* contact */
.contact-title{left:0;top:4142px;width:1200px;text-align:center;font-size:80px}
.contact-rule{left:546px;top:4232px;width:108px;height:3px;background:var(--blue)}
.footer{left:0;top:4757px;width:1200px;height:416px;background:var(--dark)}
.contact-img{left:81px;top:4329px;width:479px;height:533px;background:linear-gradient(150deg,#e9eaec 0%,#cfd3d8 40%,#6a5a50 75%,#2c2522 100%)}
.contact-form{left:560px;top:4329px;width:555px;height:533px;background:var(--panel)}
.form-lead{position:absolute;left:47px;top:36px;font-size:28px;color:#333}
.field{position:absolute;background:var(--white);border:1px solid #bbb;display:flex;align-items:flex-start;gap:10px;padding:20px 0 0 28px;font-size:21px;color:#333}
.field svg{margin-top:4px;flex:none}
.submit{position:absolute;left:43px;top:422px;width:465px;height:67px;background:var(--blue);color:var(--white);font-size:19px;display:flex;align-items:center;justify-content:center;letter-spacing:.5px}

/* footer */
.footer-brand{left:146px;top:4990px;width:230px;text-align:center}
.footer-brand .brand-name{color:var(--white);font-size:40px;width:230px}
.footer-col{color:var(--white)}
.footer-col h4{font-size:20px;font-weight:400}
.footer-col .under{width:56px;height:3px;background:var(--blue);margin:10px 0 24px}
.footer-col p{font-size:14px;line-height:19px}
.footer-col li{list-style:none;font-size:14px;line-height:26px;display:flex;align-items:center;gap:6px}
.tri{width:0;height:0;border-left:5px solid transparent;border-right:5px solid transparent;border-bottom:9px solid var(--blue)}
.dot{width:22px;height:22px;border-radius:50%;background:var(--blue)}
.copyright{left:0;top:5173px;width:1200px;height:53px;background:var(--blue-dark);color:var(--white);font-size:13px;display:flex;align-items:center;justify-content:center}
</style>
</head>
<body>

<header class="site-header abs">
  <div class="brand abs"><span class="brand-mark"></span><span class="brand-name">Keystar Capital Management</span></div>
  <nav class="main-nav abs">
    <a class="active" style="left:575px">HOME</a>
    <a style="left:656px">ABOUT US</a>
    <a style="left:766px">OUR TEAM</a>
    <a style="left:879px">INVESTMENTS</a>
    <a style="left:1017px">CONTACT US</a>
  </nav>
</header>

<section class="hero abs">
  <div class="hero-photo" role="img" aria-label="Investor in glasses looking at a trading screen with candlestick charts"></div>
  <svg class="play abs" width="96" height="96" viewBox="0 0 96 96"><circle cx="48" cy="48" r="44" fill="rgba(255,255,255,.15)" stroke="#ddd" stroke-width="5"/><path d="M38 28 L68 48 L38 68 Z" fill="#ddd"/></svg>
  <h1 class="hero-title display abs" style="color:#fff">Passion for uncovering<br>new opportunities</h1>
</section>

<section class="about">
  <div class="about-img-a abs" role="img" aria-label="Trading monitors in front of a harbour at sunset"></div>
  <div class="about-img-b abs" role="img" aria-label="Businessman in a suit checking a phone in front of market charts"></div>
  <h2 class="section-title display abs" style="left:562px;top:1012px">What we do</h2>
  <div class="eyebrow abs" style="left:570px;top:1084px">ABOUT US</div>
  <div class="body-copy abs" style="left:572px;top:1166px;width:548px">
    <p>A beacon of innovative investment where strategic diversification meets meticulous market comprehension. We navigate the complexities of Global Equities, Real Estate, Venture Capital, Private Equity, and Alternative Assets, focusing on uncovering distinctive investment opportunities for our investors.</p>
    <p style="margin-top:25px">At Keystar, investment is not just a transaction; it's a carefully orchestrated process, mirroring the meticulous management of personal assets. Our ethos is built on a bedrock of expansive market wisdom and proactive strategy formulation, ensuring our portfolio remains both robust and agile.</p>
  </div>
</section>

<section class="team">
  <h2 class="section-title display abs" style="left:81px;top:1742px;font-size:76px">Our team</h2>
  <div class="team-eyebrow abs" style="left:87px;top:1827px">MEET OUR FOUNDER</div>
  <h3 class="team-heading abs" style="left:81px;top:1896px">The Architect of Keystar's Visionary Path</h3>
  <p class="body-copy abs" style="left:81px;top:1978px;width:545px">Meet Marcus, the driving force behind Keystar Capital Management. From co-founding Australia's second-largest renewable energy company to pioneering ventures in diverse sectors, Marcus's entrepreneurial journey is marked by a passion for market innovation and sustainable growth. With over a decade of diverse business scaling experience, Marcus established Keystar Capital, evolving from personal investment to a trust-fortified endeavour of market innovation and niche investment exploration.</p>
  <div class="founder-photo abs" role="img" aria-label="Portrait of the founder in a blue suit on a city street"></div>
</section>

<section class="investments abs">
  <svg class="abs" style="left:0;top:0" width="1200" height="1624" viewBox="0 0 1200 1624">
    <polygon points="0,0 150,0 620,1624 0,1624" fill="#f4f4f4"/>
    <polygon points="900,900 1200,1624 1200,1200" fill="#e3e3e3"/>
    <polygon points="150,0 430,0 1200,1220 1200,1624" fill="#f0f0f0"/>
  </svg>
  <h2 class="inv-title display abs">Investments</h2>
  <p class="inv-intro abs">Keystar's portfolio showcases our ability to identify undervalued opportunities with significant growth potential.</p>

  <article class="card abs" style="left:171px;top:376px">
    <div class="card-img" role="img" aria-label="Two young founders presenting ideas on a whiteboard" style="background:linear-gradient(120deg,#6b4a3a,#d9dcdf 50%,#9aa3a9)"></div>
    <h3>VENTURE CAPITAL</h3><div class="rule"></div>
    <p>Strategic investments in venture capital, where we harness our industry contacts and marketunderstanding to invest in high growth startups and businesses.</p>
  </article>
  <article class="card abs" style="left:621px;top:376px">
    <div class="card-img" role="img" aria-label="Typewriter with a sheet reading private equity" style="background:linear-gradient(180deg,#e8e8e6 0%,#bfc1bd 45%,#4d5550 100%)"></div>
    <h3>PRIVATE EQUITY</h3><div class="rule"></div>
    <p>Access to investments in cutting edge sectors, featuring companies like Nova Labs, Quillstream, Datapeak, Orbitra, Synaptiq, Portway, Lumen Compute and Tallstone Games</p>
  </article>
  <article class="card abs" style="left:171px;top:975px">
    <div class="card-img" role="img" aria-label="Laptop showing stock charts with banknotes" style="background:linear-gradient(135deg,#f1f1f1 0%,#9a9a9a 45%,#2e2e2e 80%)"></div>
    <h3>GLOBAL EQUITY MARKETS</h3><div class="rule"></div>
    <p>We've demonstrated exceptional skill in identifying undervalued stocks and markets with high growth potential, leveraging in-depth research and market analysis</p>
  </article>
  <article class="card abs" style="left:621px;top:975px">
    <div class="card-img" role="img" aria-label="Glass skyscrapers against a cloudy sky" style="background:linear-gradient(180deg,#c9d7e6 0%,#8ea3b8 45%,#3d4a58 100%)"></div>
    <h3>PROPERTY DEVELOPMENT</h3><div class="rule"></div>
    <p>Curated development projects, exemplifying our ability to identify and capitalise on high-value real estate opportunities.</p>
  </article>
</section>

<h2 class="contact-title display abs">Contact us</h2>
<div class="contact-rule abs"></div>

<footer class="footer abs"></footer>

<div class="contact-img abs" role="img" aria-label="Hands holding a phone in front of a laptop with trading charts"></div>
<form class="contact-form abs">
  <div class="form-lead">Please Fill out this form</div>
  <div class="field" style="left:43px;top:101px;width:465px;height:69px">
    <svg width="18" height="20" viewBox="0 0 18 20"><circle cx="9" cy="6" r="5" fill="#0f8fd3"/><path d="M0 20 Q0 11 9 11 Q18 11 18 20Z" fill="#0f8fd3"/></svg>Name</div>
  <div class="field" style="left:43px;top:188px;width:223px;height:69px">
    <svg width="20" height="16" viewBox="0 0 20 16"><rect x="0" y="1" width="20" height="14" rx="2" fill="#0f8fd3"/><path d="M1 2 L10 9 L19 2" stroke="#fff" stroke-width="2" fill="none"/></svg>Email</div>
  <div class="field" style="left:281px;top:188px;width:225px;height:69px">
    <svg width="18" height="18" viewBox="0 0 18 18"><path d="M3 1 L7 1 L8 5 L5.5 7 Q7 11 11 12.5 L13 10 L17 11 L17 15 Q16 17 13 17 Q2 15 1 4 Q1 1 3 1Z" fill="#0f8fd3"/></svg>Number</div>
  <div class="field" style="left:43px;top:276px;width:465px;height:115px">
    <svg width="16" height="16" viewBox="0 0 16 16"><circle cx="8" cy="8" r="7" fill="#0f8fd3"/></svg>Message</div>
  <div class="submit">SUBMIT</div>
</form>

<div class="footer-brand abs"><span class="brand-name" style="display:block">Keystar Capital Management</span></div>
<div class="footer-col abs" style="left:473px;top:4950px;width:200px">
  <h4>About Us</h4><div class="under"></div>
  <p>A beacon of innovative investment where strategic diversification meets meticulous market comprehension</p>
</div>
<div class="footer-col abs" style="left:741px;top:4950px">
  <h4>Quick links</h4><div class="under"></div>
  <ul><li><span class="tri"></span>About Us</li><li><span class="tri"></span>Investors</li><li><span class="tri"></span>Our Team</li><li><span class="tri"></span>Contact Us</li></ul>
</div>
<div class="footer-col abs" style="left:936px;top:4950px">
  <h4>Follow Us</h4><div class="under"></div>
  <ul><li style="line-height:40px"><span class="dot"></span>&nbsp;Chirp</li><li style="line-height:40px"><span class="dot"></span>&nbsp;ProLink</li></ul>
</div>
<div class="copyright abs">Copyright © 2023 All Rights Reserved By Company name</div>

</body>
</html>
```